Craft brewery keg badge / badge branding to be on display on keg fonts in pubs and craft beer bars

We're a small craft beer producer and are looking to have a keg badge designed to be put onto keg fonts in bars as well as being used on our bottles. Our website is www.qlbrewery.co.uk. -Please take a look at our site however we're looking for new branding! We're not looking to have the windmill on the badge! We want a bold geometric hop design in the centre of the design. The beer is a low AVB beer (2.9% ABV) and will be hopped with Cascade, Colombus and Mosaic hops and will have a fruity / juicy aroma. We're looking to have a design that we can re-use again and again by changing: colours and wording for different beers in the future.

Target Market(s)
Craft beer drinkers
Industry/Entity Type
Craft Brewery
Requirements
Must have
- Simple, elegant, repeatable core message from the badge. It need a simple, bold geometric hop design (examples uploaded) in the centre which is repeatable across many brands in the future.
- The badge needs to be circular and 82mm across to fit our tap lenses (see http://www.velmo.co.uk/branding for the flat lens). The keg badge needs to be modern and in line with other keg badges like the examples attached- though we leave the artistic flair up to you guys. Please see below the styles of keg badge we like.
- Must be in vector file format and we must get a jpeg version too.

Should not have
- Should not be overcrowded and try to be too full of information. See attached examples.

```html
<!DOCTYPE html>
<html lang="en">
<head>
<meta charset="utf-8">
<title>Quarry Lane Brewing Company – Keg Badges</title>
<link rel="stylesheet" href="https://fonts.googleapis.com/css2?family=Bebas+Neue&family=Oswald:wght@400;500&display=swap">
<style>
  :root {
    --bg: #5b3b27;
    --white: #ffffff;
    --ink-shade: rgba(20, 12, 6, 0.45);
    --ashbury: #f3cd3b;
    --ashbury-art-a: #d9b63a;
    --ashbury-art-b: #7d5a2c;
    --millrace: #eba34f;
    --millrace-art-a: #dc9a4a;
    --millrace-art-b: #7a4a2a;
    --table: #62a4d9;
    --table-art-a: #5e94c4;
    --table-art-b: #4c6b3d;
    --furrow: #d8262e;
    --furrow-art-a: #e06a4d;
    --furrow-art-b: #b8472c;
  }
  * { margin: 0; padding: 0; box-sizing: border-box; }
  html, body { width: 1200px; height: 838px; overflow: hidden; }
  body { background: var(--bg); position: relative; }

  .badge {
    position: absolute;
    width: 358px;
    height: 358px;
  }
  .badge--ashbury  { left: 227px; top: 46px; }
  .badge--millrace { left: 618px; top: 46px; }
  .badge--table    { left: 227px; top: 438px; }
  .badge--furrow   { left: 618px; top: 438px; }

  .badge svg { width: 100%; height: 100%; display: block; }

  .badge__brand {
    font-family: "Oswald", sans-serif;
    font-size: 12px;
    letter-spacing: 1.4px;
    fill: var(--white);
    text-anchor: middle;
  }
  .badge__mark { fill: none; stroke: var(--white); stroke-width: 2.5; }
  .badge__name {
    font-family: "Bebas Neue", sans-serif;
    font-size: 40px;
    letter-spacing: 2.5px;
    fill: var(--white);
    text-anchor: middle;
  }
  .badge__style {
    font-family: "Oswald", sans-serif;
    font-size: 9px;
    letter-spacing: 1px;
    fill: var(--white);
    text-anchor: middle;
  }
  .badge__abv {
    font-family: "Bebas Neue", sans-serif;
    font-size: 34px;
    fill: var(--white);
    text-anchor: middle;
  }
  .badge__abv-unit { font-size: 14px; }
  .badge__abv-label {
    font-family: "Oswald", sans-serif;
    font-size: 6px;
    fill: var(--white);
  }
  .badge__claims {
    font-family: "Bebas Neue", sans-serif;
    font-size: 17px;
    letter-spacing: 1.5px;
    fill: var(--white);
  }

  .badge--ashbury  .badge__ring, .badge--ashbury  .badge__band { fill: var(--ashbury); }
  .badge--millrace .badge__ring, .badge--millrace .badge__band { fill: var(--millrace); }
  .badge--table    .badge__ring, .badge--table    .badge__band { fill: var(--table); }
  .badge--furrow   .badge__ring, .badge--furrow   .badge__band { fill: var(--furrow); }
</style>
</head>
<body>

<!-- Ashbury IPA -->
<div class="badge badge--ashbury">
  <svg viewBox="-197 -197 394 394">
    <defs>
      <clipPath id="clip-ashbury"><circle r="189"/></clipPath>
      <linearGradient id="art-ashbury" x1="0" y1="0" x2="0" y2="1">
        <stop offset="0" stop-color="var(--ashbury-art-a)"/>
        <stop offset="1" stop-color="var(--ashbury-art-b)"/>
      </linearGradient>
      <path id="arc-ashbury" d="M -176 0 A 176 176 0 0 0 176 0"/>
    </defs>
    <circle class="badge__ring" r="197"/>
    <g clip-path="url(#clip-ashbury)">
      <rect x="-189" y="-189" width="378" height="378" fill="url(#art-ashbury)" role="img" aria-label="Painted illustration of a windmill under a cloudy golden sky"/>
      <rect x="-189" y="88" width="378" height="101" fill="var(--ink-shade)"/>
      <rect class="badge__band" x="-189" y="50" width="378" height="38"/>
    </g>
    <circle class="badge__mark" cy="-50" r="24"/>
    <text class="badge__brand" y="22">QUARRY LANE</text>
    <text class="badge__brand" y="38">BREWING COMPANY</text>
    <text class="badge__name" y="84">ASHBURY IPA</text>
    <text class="badge__style" y="104">STRONG CLASSIC BRITISH ALE</text>
    <text class="badge__abv" y="147">4.2<tspan class="badge__abv-unit" dy="-15">%</tspan></text>
    <text class="badge__abv-label" x="18" y="147">ABV</text>
    <text class="badge__claims"><textPath href="#arc-ashbury" startOffset="50%" text-anchor="middle">UNFINED • UNFILTERED • VEGAN</textPath></text>
  </svg>
</div>

<!-- Millrace APA -->
<div class="badge badge--millrace">
  <svg viewBox="-197 -197 394 394">
    <defs>
      <clipPath id="clip-millrace"><circle r="189"/></clipPath>
      <linearGradient id="art-millrace" x1="0" y1="0" x2="0" y2="1">
        <stop offset="0" stop-color="var(--millrace-art-a)"/>
        <stop offset="1" stop-color="var(--millrace-art-b)"/>
      </linearGradient>
      <path id="arc-millrace" d="M -176 0 A 176 176 0 0 0 176 0"/>
    </defs>
    <circle class="badge__ring" r="197"/>
    <g clip-path="url(#clip-millrace)">
      <rect x="-189" y="-189" width="378" height="378" fill="url(#art-millrace)" role="img" aria-label="Painted illustration of a windmill under a cloudy amber sky"/>
      <rect x="-189" y="88" width="378" height="101" fill="var(--ink-shade)"/>
      <rect class="badge__band" x="-189" y="50" width="378" height="38"/>
    </g>
    <circle class="badge__mark" cy="-50" r="24"/>
    <text class="badge__brand" y="22">QUARRY LANE</text>
    <text class="badge__brand" y="38">BREWING COMPANY</text>
    <text class="badge__name" y="84">MILLRACE APA</text>
    <text class="badge__style" y="104">DDH APA: CASCADE, EUREKA, COLUMBUS, AND VIC SECRET</text>
    <text class="badge__abv" y="147">4.5<tspan class="badge__abv-unit" dy="-15">%</tspan></text>
    <text class="badge__abv-label" x="18" y="147">ABV</text>
    <text class="badge__claims"><textPath href="#arc-millrace" startOffset="50%" text-anchor="middle">UNFINED • UNFILTERED • VEGAN</textPath></text>
  </svg>
</div>

<!-- Table Beer -->
<div class="badge badge--table">
  <svg viewBox="-197 -197 394 394">
    <defs>
      <clipPath id="clip-table"><circle r="189"/></clipPath>
      <linearGradient id="art-table" x1="0" y1="0" x2="0" y2="1">
        <stop offset="0" stop-color="var(--table-art-a)"/>
        <stop offset="1" stop-color="var(--table-art-b)"/>
      </linearGradient>
      <path id="arc-table" d="M -176 0 A 176 176 0 0 0 176 0"/>
    </defs>
    <circle class="badge__ring" r="197"/>
    <g clip-path="url(#clip-table)">
      <rect x="-189" y="-189" width="378" height="378" fill="url(#art-table)" role="img" aria-label="Painted illustration of a windmill under a cloudy blue sky"/>
      <rect x="-189" y="88" width="378" height="101" fill="var(--ink-shade)"/>
      <rect class="badge__band" x="-189" y="50" width="378" height="38"/>
    </g>
    <circle class="badge__mark" cy="-50" r="24"/>
    <text class="badge__brand" y="22">QUARRY LANE</text>
    <text class="badge__brand" y="38">BREWING COMPANY</text>
    <text class="badge__name" y="84">TABLE BEER</text>
    <text class="badge__style" y="104">PALE ALE: CASCADE, COLUMBUS, AND MOSAIC</text>
    <text class="badge__abv" y="147">2.9<tspan class="badge__abv-unit" dy="-15">%</tspan></text>
    <text class="badge__abv-label" x="18" y="147">ABV</text>
    <text class="badge__claims"><textPath href="#arc-table" startOffset="50%" text-anchor="middle">UNFINED • UNFILTERED • VEGAN</textPath></text>
  </svg>
</div>

<!-- The Long Furrow IPA -->
<div class="badge badge--furrow">
  <svg viewBox="-197 -197 394 394">
    <defs>
      <clipPath id="clip-furrow"><circle r="189"/></clipPath>
      <linearGradient id="art-furrow" x1="0" y1="0" x2="0" y2="1">
        <stop offset="0" stop-color="var(--furrow-art-a)"/>
        <stop offset="1" stop-color="var(--furrow-art-b)"/>
      </linearGradient>
      <path id="arc-furrow" d="M -176 0 A 176 176 0 0 0 176 0"/>
    </defs>
    <circle class="badge__ring" r="197"/>
    <g clip-path="url(#clip-furrow)">
      <rect x="-189" y="-189" width="378" height="378" fill="url(#art-furrow)" role="img" aria-label="Painted illustration of a windmill under a cloudy red sky"/>
      <rect x="-189" y="88" width="378" height="101" fill="var(--ink-shade)"/>
      <rect class="badge__band" x="-189" y="50" width="378" height="38"/>
    </g>
    <circle class="badge__mark" cy="-50" r="24"/>
    <text class="badge__brand" y="22">QUARRY LANE</text>
    <text class="badge__brand" y="38">BREWING COMPANY</text>
    <text class="badge__name" y="84">THE LONG FURROW IPA</text>
    <text class="badge__style" y="104">PALE ALE: CASCADE, COLUMBUS, AND MOSAIC</text>
    <text class="badge__abv" y="147">4.5<tspan class="badge__abv-unit" dy="-15">%</tspan></text>
    <text class="badge__abv-label" x="18" y="147">ABV</text>
    <text class="badge__claims"><textPath href="#arc-furrow" startOffset="50%" text-anchor="middle">UNFINED • UNFILTERED • VEGAN</textPath></text>
  </svg>
</div>

</body>
</html>
```